Vessa Kliniq - Dermatology Consultation App

Vessa Kliniq is launching a new Pindle IOS App for online Dermatology consultation. We would appreciate a simple Scandinavian design which communicates trust, comfort and expensive feel. Most yacht designs have similar color palette, light wood colors and textures, but don’t be restricted by those in your artistic search.
The process is completed in three easy steps:
1. take a Snapshot.
2. Describe and Send it.
3. get Diagnosis and Treatment.
The Home screen should also have buttons - Start new Case, Follow up Visit, Rx Refill.
15% of the Home screen should also have a field/button - Medical Cosmetics Shop.
10% of the Home screen should also have a field or buttons for Our Partners (sponsors) – Lumavel, Norvexa, Toral, Ostra. (if you click you would be directed to their sites)
Note / Suggestion : Maybe you could use a larger picture of a dermatologist and have overlying fields and content, just for more influencing effect. (I am not a professional though)
Thank you so much.
24 - 59 Female
Club

```html
<!DOCTYPE html>
<html lang="en">
<head>
<meta charset="UTF-8">
<title>Vessa Kliniq – Home</title>
<link rel="stylesheet" href="https://fonts.googleapis.com/css2?family=Cormorant+Garamond:wght@400&family=Open+Sans:wght@300;400&display=swap">
<style>
  :root {
    --screen-bg: #f7f7f7;
    --photo-light: #eeeeee;
    --photo-mid: #d8d8d8;
    --text-main: #555555;
    --text-soft: #7a7a7a;
    --tick-grey: #6d6d6d;
    --tick-accent: #e8925a;
    --btn-light: #cccccc;
    --btn-dark: #b0b0b0;
    --btn-text: #ffffff;
    --outline: #b9b9b9;
    --partner: #8a8a8a;
  }
  * { box-sizing: border-box; margin: 0; padding: 0; }
  html, body { width: 781px; height: 1200px; overflow: hidden; }
  body {
    background: var(--screen-bg);
    font-family: "Open Sans", sans-serif;
    color: var(--text-main);
    position: relative;
  }
  .hero-photo {
    position: absolute;
    inset: 0;
    background:
      radial-gradient(ellipse 340px 560px at 200px 360px, var(--photo-mid) 0%, rgba(216,216,216,0.4) 55%, rgba(247,247,247,0) 100%),
      radial-gradient(ellipse 260px 320px at 560px 820px, var(--photo-light) 0%, rgba(247,247,247,0) 100%);
    opacity: 0.85;
  }
  .screen { position: relative; width: 100%; height: 100%; }
  .brand-name {
    position: absolute;
    top: 132px; left: 0; right: 0;
    text-align: center;
    font-family: "Cormorant Garamond", serif;
    font-weight: 400;
    font-size: 60px;
    line-height: 72px;
    color: var(--text-main);
    letter-spacing: 1px;
  }
  .tagline {
    position: absolute; top: 274px; left: 0; right: 0;
    text-align: center;
    font-size: 24px; font-weight: 400;
    color: var(--text-main);
  }
  .steps {
    position: absolute; top: 470px; left: 230px;
    list-style: none;
  }
  .step {
    display: flex; align-items: center; gap: 26px;
    height: 100px;
    font-size: 32px; font-weight: 300;
    color: var(--text-main);
  }
  .step:nth-child(2) { margin-left: -14px; }
  .step:nth-child(3) { margin-left: 6px; }
  .step svg { width: 42px; height: 42px; flex: none; }
  .shop-link {
    position: absolute; top: 850px; left: 50%;
    transform: translateX(-50%);
    width: 230px; height: 46px;
    border: 2px solid var(--outline);
    border-radius: 6px;
    display: flex; align-items: center; justify-content: center;
    font-size: 20px; color: var(--text-soft);
    background: rgba(255,255,255,0.4);
  }
  .actions {
    position: absolute; top: 950px; left: 26px; right: 26px;
    display: flex; gap: 28px;
  }
  .btn {
    flex: 1; height: 70px; border-radius: 8px;
    display: flex; align-items: center; justify-content: center;
    font-size: 26px; color: var(--btn-text); font-weight: 400;
  }
  .btn-start { background: var(--btn-light); }
  .btn-signin { background: var(--btn-dark); }
  .partners {
    position: absolute; top: 1105px; left: 40px; right: 40px;
    display: flex; justify-content: space-between; align-items: center;
    font-size: 26px; color: var(--partner); font-weight: 400;
  }
</style>
</head>
<body>
  <div class="hero-photo" role="img" aria-label="Soft faded photograph of a woman touching her shoulder"></div>
  <main class="screen">
    <header class="brand-name">Vessa Kliniq</header>
    <p class="tagline">Real Doctor Dermatology Consultation</p>

    <ol class="steps">
      <li class="step">
        <svg viewBox="0 0 42 42"><circle cx="21" cy="21" r="18" fill="none" stroke="var(--tick-grey)" stroke-width="2.5"/><path d="M13 21l6 6 13-14" fill="none" stroke="var(--tick-grey)" stroke-width="3"/></svg>
        Take a Snapshot
      </li>
      <li class="step">
        <svg viewBox="0 0 42 42"><circle cx="21" cy="21" r="18" fill="none" stroke="var(--tick-grey)" stroke-width="2.5"/><path d="M13 21l6 6 13-14" fill="none" stroke="var(--tick-grey)" stroke-width="3"/></svg>
        Describe and Send it
      </li>
      <li class="step">
        <svg viewBox="0 0 42 42"><circle cx="21" cy="21" r="18" fill="none" stroke="var(--tick-accent)" stroke-width="2.5"/><path d="M13 21l6 6 13-14" fill="none" stroke="var(--tick-accent)" stroke-width="3"/></svg>
        Get Diagnosed
      </li>
    </ol>

    <div class="shop-link">Medical Cosmetics</div>

    <nav class="actions">
      <div class="btn btn-start">Start</div>
      <div class="btn btn-signin">Sign In</div>
    </nav>

    <footer class="partners">
      <span>Ostra</span>
      <span>Toral</span>
      <span>Norvexa</span>
      <span>Lumavel</span>
    </footer>
  </main>
</body>
</html>
```